I need a business card for my original fine art pieces

I would like a business card design including a logo design for a new business in the art world. I am based in the Hunter Valley NSW Australia. I am a contemporary figurative, encaustic and wildlife artist. I would like to be able to upload my email and mobile number to this as well. This design should be one that I can incorporate into banners and flyers etc. Id like to incorporate one of my own images or partial image into the background or somewhere below. My initials are KR and I would like these used as a logo type. I would like the use of some colour and it to be bright and catchy. The final design should communicate artwork custom made and commissions available.

Overview: Original Fine Artworks for sale, online, art galleries etc, Custom made to order and by commission.

Target market is world wide audience and corporate world

My figurative work is painted using acrylics in a lot of natural ochre colours that reflect the Australian Outback, on canvas, linen, paper or board: My encaustic work is created in a contemporary abstract style using a blow torch and a made with a medium of 100% pure bees wax, Damar resin, mixed media and coloured pigments, applied to Birch board. My wildlife are created using coloured pencil and mixed media on a variety of paper types or board.

```html
<!DOCTYPE html>
<html lang="en">
<head>
<meta charset="utf-8">
<title>Kira Rowan – Artist Business Card</title>
<link rel="stylesheet" href="https://fonts.googleapis.com/css2?family=UnifrakturMaguntia&family=Italianno&display=swap">
<style>
  :root {
    --card-grey: #c9c7cf;
    --band-light: #e9e6e9;
    --ink-blue: #000e87;
    --mark-grey: #555457;
    --name-brown: #5a3030;
    --splash-yellow: #e6e36e;
    --splash-olive: #7a7f45;
    --splash-brown: #6e5353;
    --splash-plum: #3c2a45;
    --splash-navy: #0b124f;
    --ornament-tone: #bdb7c0;
    --icon-white: #ffffff;
  }
  html, body {
    margin: 0;
    padding: 0;
    width: 1200px;
    height: 686px;
    overflow: hidden;
    background: var(--card-grey);
  }
  .business-card {
    display: block;
    width: 1200px;
    height: 686px;
  }
  .card-base { fill: var(--card-grey); }
  .light-band { fill: var(--band-light); }
  .blue-wave { fill: var(--ink-blue); }
  .name-banner { fill: #ffffff; fill-opacity: 0.45; }
  .corner-ornament { fill: var(--ornament-tone); }
  .brand-dot { fill: var(--mark-grey); }
  .brand-initials {
    font-family: "UnifrakturMaguntia", serif;
    font-size: 64px;
    fill: var(--mark-grey);
  }
  .artist-name {
    font-family: "UnifrakturMaguntia", serif;
    font-size: 50px;
    fill: var(--name-brown);
  }
  .artist-title {
    font-family: "Italianno", cursive;
    font-size: 40px;
    fill: var(--name-brown);
  }
  .splash-yellow { fill: var(--splash-yellow); fill-opacity: 0.9; }
  .splash-olive { fill: var(--splash-olive); }
  .splash-brown { fill: var(--splash-brown); }
  .splash-plum { fill: var(--splash-plum); }
  .splash-navy { fill: var(--splash-navy); }
  .contact-icon {
    fill: none;
    stroke: var(--icon-white);
    stroke-width: 1.6;
    stroke-linejoin: round;
  }
  .contact-icon-solid { fill: var(--icon-white); }
</style>
</head>
<body>
<svg class="business-card" viewBox="0 0 1051 602" width="1200" height="686" xmlns="http://www.w3.org/2000/svg">
  <rect class="card-base" x="0" y="0" width="1051" height="602"/>

  <rect class="corner-ornament" role="img" aria-label="Decorative floral medallion" x="20" y="10" width="96" height="96" rx="48"/>
  <rect class="corner-ornament" role="img" aria-label="Decorative floral medallion" x="940" y="10" width="96" height="96" rx="48"/>

  <rect class="light-band" x="0" y="417" width="1051" height="52"/>
  <path class="blue-wave" d="M0 467 H625 C700 467 740 420 790 340 C840 255 900 170 1051 150 V602 H0 Z"/>

  <polygon class="name-banner" points="492,171 1051,171 1051,284 600,284"/>

  <g class="brand-mark">
    <circle class="brand-dot" cx="188" cy="228" r="38"/>
    <text class="brand-initials" x="240" y="252">KR</text>
  </g>

  <g class="artist-heading">
    <text class="artist-name" x="1012" y="228" text-anchor="end">Kira Rowan</text>
    <text class="artist-title" x="926" y="270" text-anchor="end">Artist</text>
  </g>

  <g class="paint-splashes" role="img" aria-label="Paint splatter accents">
    <circle class="splash-yellow" cx="702" cy="304" r="38"/>
    <circle class="splash-yellow" cx="697" cy="386" r="35"/>
    <circle class="splash-yellow" cx="766" cy="370" r="17"/>
    <circle class="splash-yellow" cx="735" cy="368" r="9"/>
    <circle class="splash-olive" cx="832" cy="376" r="27"/>
    <circle class="splash-olive" cx="809" cy="468" r="31"/>
    <circle class="splash-olive" cx="880" cy="405" r="8"/>
    <circle class="splash-olive" cx="852" cy="398" r="6"/>
    <circle class="splash-olive" cx="779" cy="577" r="5"/>
    <circle class="splash-brown" cx="71" cy="388" r="14"/>
    <circle class="splash-brown" cx="91" cy="438" r="15"/>
    <circle class="splash-brown" cx="125" cy="421" r="14"/>
    <circle class="splash-plum" cx="74" cy="498" r="14"/>
    <circle class="splash-navy" cx="998" cy="548" r="22"/>
    <circle class="splash-navy" cx="983" cy="521" r="5"/>
  </g>

  <g class="email-icon">
    <rect class="contact-icon" x="176" y="478" width="30" height="21"/>
    <polyline class="contact-icon" points="176,478 191,491 206,478"/>
  </g>

  <g class="phone-icon">
    <rect class="contact-icon" x="183" y="532" width="14" height="32" rx="2" transform="rotate(-10 190 548)"/>
    <line class="contact-icon" x1="191" y1="531" x2="189" y2="522"/>
    <rect class="contact-icon" x="186" y="537" width="8" height="8" transform="rotate(-10 190 541)"/>
  </g>

  <g class="chat-icon">
    <ellipse class="contact-icon-solid" cx="560" cy="497" rx="13" ry="9"/>
    <polygon class="contact-icon-solid" points="552,503 548,511 558,505"/>
    <ellipse class="contact-icon-solid" cx="580" cy="486" rx="12" ry="8"/>
    <polygon class="contact-icon-solid" points="586,491 590,498 580,493"/>
    <ellipse class="contact-icon-solid" cx="574" cy="510" rx="12" ry="8"/>
    <polygon class="contact-icon-solid" points="568,515 565,521 574,516"/>
  </g>
</svg>
</body>
</html>
```